Personal Injury Billboard for a law frim

Our firm has a billboard we need art for. It will specifically for personal injury cases. The dimensions of art the billboard are 9 ft high 29 feet wide.

We want to highlight the terms, "Serious Injuries" and "Trusted. Local. Experienced." We want to incorporate the attached "Brightvale Honors" badge as well as our attached firm logo. We want the blue color scheme (see attached).

Maybe an image of an industrial plant in the background?

Sans Serif

```html
<!DOCTYPE html>
<html lang="en">
<head>
<meta charset="utf-8">
<title>Serious Injuries Billboard – Halvern Brooks Raine Attorneys</title>
<link href="https://fonts.googleapis.com/css2?family=League+Gothic&family=Oswald:wght@600&family=Poppins:wght@400;500;600&display=swap" rel="stylesheet">
<style>
  :root {
    --navy: #0b2a6b;
    --blue: #3a8fd6;
    --blue-deep: #1d5fb8;
    --ink: #1c2233;
    --page: #eef0f2;
    --sky-top: #dfe6ee;
    --sky-mid: #c9d3de;
    --plant: #aab6c3;
    --white: #ffffff;
  }
  * { margin: 0; padding: 0; box-sizing: border-box; }
  html, body {
    width: 1200px;
    height: 800px;
    overflow: hidden;
    background: var(--page);
  }
  .billboard {
    position: absolute;
    left: 20px;
    top: 190px;
    width: 1160px;
    height: 420px;
    overflow: hidden;
    font-family: "Poppins", sans-serif;
  }
  .backdrop {
    position: absolute;
    inset: 0;
    background: linear-gradient(180deg, var(--sky-top) 0%, var(--sky-mid) 55%, var(--plant) 100%);
    opacity: 0.85;
  }
  .brand {
    position: absolute;
    left: 40px;
    top: 80px;
    width: 250px;
    text-align: center;
  }
  .brand-mark {
    display: flex;
    align-items: center;
    justify-content: center;
    gap: 10px;
    height: 160px;
  }
  .brand-square {
    width: 34px;
    height: 34px;
    background: var(--blue-deep);
  }
  .brand-name {
    font-family: "Oswald", sans-serif;
    font-weight: 600;
    font-size: 72px;
    color: var(--blue-deep);
    letter-spacing: 4px;
  }
  .brand-url {
    margin-top: 6px;
    font-size: 15px;
    color: var(--blue-deep);
    text-decoration: underline;
  }
  .brand-firm {
    margin-top: 4px;
    font-size: 17px;
    font-weight: 500;
    color: var(--ink);
    letter-spacing: 0.3px;
  }
  .brand-role {
    display: flex;
    align-items: center;
    gap: 6px;
    font-size: 10px;
    font-weight: 500;
    letter-spacing: 1px;
    color: var(--ink);
    padding: 0 4px;
  }
  .brand-role::before,
  .brand-role::after {
    content: "";
    flex: 1;
    height: 1px;
    background: var(--ink);
  }
  .divider {
    position: absolute;
    left: 346px;
    top: 45px;
    width: 5px;
    height: 316px;
    background: var(--blue-deep);
  }
  .headline {
    position: absolute;
    left: 412px;
    top: 96px;
    width: 684px;
    font-family: "League Gothic", sans-serif;
    font-size: 150px;
    line-height: 1;
    color: var(--navy);
    text-align: center;
    letter-spacing: 1px;
    white-space: nowrap;
  }
  .tagline {
    position: absolute;
    left: 412px;
    top: 246px;
    width: 684px;
    height: 64px;
    background: var(--blue);
    border: 1px solid var(--blue-deep);
    color: var(--white);
    font-family: "Oswald", sans-serif;
    font-weight: 600;
    font-size: 44px;
    line-height: 62px;
    text-align: center;
    letter-spacing: 1px;
  }
  .contacts {
    position: absolute;
    left: 412px;
    top: 356px;
    width: 720px;
    display: flex;
    gap: 22px;
    font-size: 15px;
    color: var(--ink);
    white-space: nowrap;
  }
  .contact-label {
    font-weight: 600;
    color: var(--navy);
    margin-right: 6px;
  }
  .base-band {
    position: absolute;
    left: 0;
    bottom: 0;
    width: 100%;
    height: 12px;
    background: linear-gradient(90deg, var(--blue) 0%, var(--blue-deep) 100%);
  }
</style>
</head>
<body>
  <main class="billboard">
    <div class="backdrop" role="img" aria-label="Faded photograph of an industrial plant with smokestacks and cooling towers under a grey sky"></div>

    <div class="brand">
      <div class="brand-mark">
        <span class="brand-square"></span>
        <span class="brand-name">HBR</span>
      </div>
      <p class="brand-url">www.hbr-law.com</p>
      <p class="brand-firm">HALVERN BROOKS RAINE</p>
      <p class="brand-role">ATTORNEYS</p>
    </div>

    <div class="divider"></div>

    <h1 class="headline">SERIOUS INJURIES</h1>
    <p class="tagline">TRUSTED. LOCAL. EXPERIENCED</p>

    <div class="contacts">
      <p><span class="contact-label">Production Contact:</span>tnolan@ferrisgate.com</p>
      <p><span class="contact-label">Media Contact:</span>jlarke@ferrisgate.com</p>
    </div>

    <div class="base-band"></div>
  </main>
</body>
</html>
```